Real Estate "For Sale" Sign for construction company

We need a sign that we can use to hang on a post and place on the road when we sell a property. The sign will be simple and will need to mainly feature our logo (files attached), as well as the words "For Sale", and then our phone number "(555) 617 3489". The sign will hang on a post that'll look something like the attached picture.

Target Market(s)

Home buyers

Industry/Entity Type

Real Estate

Font styles to use
Serif
Sans Serif

Colors
0054AA
0677BA
7BADD7
CADEEF
E8F1F8
0094D4
00A9DD
6FCCEA
C7EBF8
E9F6FB

Requirements
Must have
• For Sale & our phone number

```html
<!DOCTYPE html>
<html lang="en">
<head>
<meta charset="UTF-8">
<title>For Sale Sign – Highland Oak Properties</title>
<link rel="stylesheet" href="https://fonts.googleapis.com/css2?family=Archivo+Black&family=Montserrat:wght@500&family=Roboto+Condensed:wght@700&family=Yellowtail&display=swap">
<style>
  :root {
    --backdrop: #808080;
    --blue-deep: #0a62b2;
    --blue-mid: #0677ba;
    --blue-bright: #1fa3de;
    --blue-outline: #1a7fc8;
    --sky: #45c4f0;
    --sky-dark: #2fa6df;
    --white: #ffffff;
    --logo-ink: #0a6fb8;
    --logo-mark: #1d4f9a;
  }
  html, body {
    margin: 0;
    width: 1200px;
    height: 1200px;
    overflow: hidden;
    background: var(--backdrop);
  }
  .sign {
    position: absolute;
    left: 185px;
    top: 79px;
    width: 830px;
    height: 1040px;
    display: block;
  }
  .sign-for {
    font-family: "Yellowtail", cursive;
    fill: var(--white);
  }
  .sign-sale {
    font-family: "Archivo Black", sans-serif;
  }
  .sign-phone {
    font-family: "Roboto Condensed", sans-serif;
    font-weight: 700;
    fill: var(--white);
  }
  .brand-name {
    font-family: "Montserrat", sans-serif;
    font-weight: 500;
    fill: var(--logo-ink);
  }
</style>
</head>
<body>
<svg class="sign" viewBox="0 0 664 832" xmlns="http://www.w3.org/2000/svg" role="img" aria-label="For Sale sign for Highland Oak Properties, call (555) 617 3489">
  <defs>
    <linearGradient id="sign-bg" x1="0" y1="1" x2="1" y2="0">
      <stop offset="0" stop-color="var(--blue-deep)"/>
      <stop offset="0.55" stop-color="var(--blue-mid)"/>
      <stop offset="1" stop-color="var(--blue-bright)"/>
    </linearGradient>
  </defs>

  <rect class="sign-field" width="664" height="832" fill="url(#sign-bg)"/>

  <g class="headline">
    <text class="sign-for" x="282" y="170" font-size="100" text-anchor="middle" transform="rotate(-8 282 150)">For</text>

    <g class="sign-sale" transform="rotate(-6 330 270)" font-size="235" text-anchor="middle">
      <text x="330" y="375" textLength="540" lengthAdjust="spacingAndGlyphs" fill="none" stroke="var(--white)" stroke-width="26" stroke-linejoin="round">SALE</text>
      <text x="330" y="375" textLength="540" lengthAdjust="spacingAndGlyphs" fill="none" stroke="var(--blue-outline)" stroke-width="22" stroke-linejoin="round">SALE</text>
      <text x="330" y="375" textLength="540" lengthAdjust="spacingAndGlyphs" fill="var(--white)">SALE</text>
    </g>
  </g>

  <g class="phone-ribbon" transform="translate(332 458) rotate(-8)">
    <polygon class="ribbon-tail" points="-262,20 -190,50 -280,112" fill="var(--sky-dark)"/>
    <rect class="ribbon-band" x="-262" y="-44" width="520" height="88" fill="var(--sky)"/>
    <text class="sign-phone" x="-2" y="28" font-size="78" text-anchor="middle" textLength="470" lengthAdjust="spacingAndGlyphs">(555) 617 3489</text>
  </g>

  <g class="footer">
    <path class="footer-arc" d="M0 712 Q332 428 664 680 L664 832 L0 832 Z" fill="var(--sky)"/>
    <path class="footer-panel" d="M0 750 Q332 458 664 715 L664 832 L0 832 Z" fill="var(--white)"/>
  </g>

  <g class="brand">
    <circle class="brand-mark" cx="332" cy="675" r="42" fill="var(--logo-mark)"/>
    <text class="brand-name" x="332" y="755" font-size="34" text-anchor="middle">Highland Oak Properties</text>
  </g>
</svg>
</body>
</html>
```